Stationery Design needed for logo design project

This project is linked to Professional firm of accountants need a make over. Our company needs a Stationery Design. Please refer to our original project in the link above.

Industry/Entity Type

It Company

Requirements
Must have
• We have three offices , so headed note paper for each office seperately
Nice to have
• we like clean uncomplicated designs, as we are happy with the logo as is and don't want to distract from it
Should not have
• there needs to be a legend at the bottom of the paper setting out our obligations under the council of meridian harbourmasters

```html
<!DOCTYPE html>
<html lang="en">
<head>
<meta charset="utf-8">
<title>Corvella Stationery</title>
<link href="https://fonts.googleapis.com/css2?family=Didact+Gothic&family=Arimo:wght@400;700&display=swap" rel="stylesheet">
<style>
  :root {
    --bg: #efefef;
    --paper: #ffffff;
    --edge: #dcdcdc;
    --ink: #3a3a3a;
    --ink-soft: #6b6b6b;
    --brand-grey: #6f6f6f;
    --brand-green: #2fc83a;
    --rule: #9a9a9a;
    --fax-title: #7a7a7a;
    --signature: #5566b8;
  }
  * { margin: 0; padding: 0; box-sizing: border-box; }
  html, body { width: 1200px; height: 815px; overflow: hidden; }
  body { background: var(--bg); font-family: "Didact Gothic", sans-serif; color: var(--ink); position: relative; }

  .sheet { position: absolute; top: 72px; width: 483px; height: 680px; background: var(--paper); border: 1px solid var(--edge); }
  .sheet--letter { left: 80px; }
  .sheet--fax { left: 638px; }

  .brand { position: absolute; left: 36px; top: 38px; display: flex; align-items: center; gap: 12px; }
  .brand__mark { width: 14px; height: 14px; background: var(--brand-green); }
  .brand__name { font-size: 26px; line-height: 26px; color: var(--brand-grey); letter-spacing: 0.5px; }
  .brand__tagline { font-size: 10px; color: var(--brand-grey); margin-top: 1px; }

  .letter__salutation { position: absolute; left: 35px; top: 146px; font-size: 12px; font-weight: 700; font-family: "Arimo", sans-serif; }
  .letter__body { position: absolute; left: 35px; top: 172px; width: 410px; font-size: 8.1px; line-height: 10.6px; text-align: justify; color: var(--ink); }
  .letter__body p { margin-bottom: 10.6px; }
  .letter__signature { position: absolute; left: 245px; top: 494px; width: 112px; height: 66px; background: linear-gradient(135deg, rgba(85,102,184,0.12), rgba(85,102,184,0.28)); }
  .letter__closing { position: absolute; right: 40px; top: 504px; text-align: right; font-size: 8.5px; color: var(--ink-soft); }
  .letter__signatory { display: block; margin-top: 5px; font-family: "Arimo", sans-serif; font-weight: 700; font-size: 12px; color: var(--ink); }

  .contact { position: absolute; left: 33px; top: 638px; display: flex; font-size: 7px; line-height: 10px; color: var(--ink-soft); }
  .contact__group { padding: 0 12px 0 0; margin-right: 12px; border-right: 1px solid var(--edge); }
  .contact__group:last-child { border-right: 0; }
  .contact__line { display: flex; align-items: center; gap: 4px; }
  .contact__icon { width: 7px; height: 7px; background: var(--brand-green); border-radius: 1px; }

  .fax__title { position: absolute; right: 30px; top: 34px; font-family: "Arimo", sans-serif; font-size: 62px; line-height: 62px; color: var(--fax-title); }
  .fax__details { position: absolute; left: 23px; top: 140px; width: 437px; border-collapse: collapse; font-family: "Arimo", sans-serif; font-size: 7.5px; font-weight: 700; color: var(--ink); }
  .fax__details td { border: 1px solid var(--rule); height: 14.3px; padding: 0 4px; }
  .fax__details .label { width: 47px; }
  .fax__details .field { width: 172px; }
  .fax__notes { position: absolute; left: 23px; top: 227px; width: 437px; height: 327px; border: 1px solid var(--rule); }
  .fax__flags { display: flex; height: 15px; border-bottom: 1px solid var(--rule); background: #f4f4f4; font-family: "Arimo", sans-serif; font-size: 7.5px; font-weight: 700; color: var(--ink-soft); }
  .fax__flag { display: flex; align-items: center; justify-content: center; gap: 4px; border-right: 1px solid var(--rule); }
  .fax__flag:last-child { border-right: 0; }
  .fax__box { width: 6px; height: 6px; border: 1px solid var(--rule); background: var(--paper); }
  .fax__comments-label { text-align: center; margin-top: 10px; font-family: "Arimo", sans-serif; font-size: 7.5px; color: var(--ink-soft); }
</style>
</head>
<body>

<section class="sheet sheet--letter">
  <header class="brand">
    <span class="brand__mark"></span>
    <div>
      <div class="brand__name">corvella</div>
      <div class="brand__tagline">Chartered Accountants</div>
    </div>
  </header>

  <p class="letter__salutation">Dear sir / madame,</p>
  <div class="letter__body">
    <p>Lorem ipsum dolor sit amet, consectetur adipisicing elit, sed do eiusmod tempor incididunt ut labore et dolore magna aliqua. Ut enim ad minim veniam, quis nostrud exercitation ullamco laboris nisi ut aliquip ex ea commodo consequat. Duis aute irure dolor in reprehenderit in voluptate velit esse cillum dolore eu fugiat nulla pariatur. Excepteur sint occaecat cupidatat non proident, sunt in culpa qui officia deserunt mollit anim id est laborum.Lorem ipsum dolor sit amet, consectetur adipisicing elit, sed do eiusmod tempor incididunt ut labore et dolore magna aliqua. Ut enim ad minim veniam, quis nostrud exercitation ullamco laboris nisi ut aliquip ex ea commodo consequat. Duis aute irure dolor in reprehenderit in voluptate velit esse cillum dolore eu fugiat nulla pariatur. Excepteur sint occaecat cupidatat non proident, sunt in culpa qui officia deserunt mollit anim id est laborum.</p>
    <p>Lorem ipsum dolor sit amet, consectetur adipisicing elit, sed do eiusmod tempor incididunt ut labore et dolore magna aliqua. Ut enim ad minim veniam, quis nostrud exercitation ullamco laboris nisi ut aliquip ex ea commodo consequat. Duis aute irure dolor in reprehenderit in voluptate velit esse cillum dolore eu fugiat nulla pariatur. Excepteur sint occaecat cupidatat non proident, sunt in culpa qui officia deserunt mollit anim id est laborum.</p>
    <p>Lorem ipsum dolor sit amet, consectetur adipisicing elit, sed do eiusmod tempor incididunt ut labore et dolore magna aliqua. Ut enim ad minim veniam, quis nostrud exercitation ullamco laboris nisi ut aliquip ex ea commodo consequat. Duis aute irure dolor in reprehenderit in voluptate velit esse cillum dolore eu fugiat nulla pariatur. Excepteur sint occaecat cupidatat non proident, sunt in culpa qui officia deserunt mollit anim id est laborum.</p>
    <p>Lorem ipsum dolor sit amet, consectetur adipisicing elit, sed do eiusmod tempor incididunt ut labore et dolore magna aliqua. Ut enim ad minim veniam, quis nostrud exercitation ullamco laboris nisi ut aliquip ex ea commodo consequat. Duis aute irure dolor in reprehenderit in voluptate velit esse cillum dolore eu fugiat nulla pariatur. Excepteur sint occaecat cupidatat non proident, sunt in culpa qui officia deserunt mollit anim id est laborum.</p>
  </div>

  <div class="letter__signature" role="img" aria-label="Handwritten signature of the signatory"></div>
  <p class="letter__closing">Yours Sincerely,<span class="letter__signatory">Lena Harrow</span></p>

  <footer class="contact">
    <div class="contact__group">
      <div class="contact__line"><span class="contact__icon"></span>(07) 5120 4417</div>
      <div class="contact__line"><span class="contact__icon"></span>(07) 5120 4418</div>
    </div>
    <div class="contact__group">
      <div class="contact__line"><span class="contact__icon"></span>info@corvella.com</div>
      <div class="contact__line"><span class="contact__icon"></span>www.corvella.com</div>
    </div>
    <div class="contact__group">
      <div>Suite 4, 208B</div>
      <div>Riverton QLD</div>
    </div>
  </footer>
</section>

<section class="sheet sheet--fax">
  <header class="brand">
    <span class="brand__mark"></span>
    <div>
      <div class="brand__name">corvella</div>
      <div class="brand__tagline">Chartered Accountants</div>
    </div>
  </header>
  <h1 class="fax__title">FAX</h1>

  <table class="fax__details">
    <tr><td class="label">To:</td><td class="field"></td><td class="label">From:</td><td class="field"></td></tr>
    <tr><td class="label">Fax:</td><td class="field"></td><td class="label">Pages:</td><td class="field"></td></tr>
    <tr><td class="label">Phone:</td><td class="field"></td><td class="label">Date:</td><td class="field"></td></tr>
    <tr><td class="label">Re:</td><td class="field"></td><td class="label">CC:</td><td class="field"></td></tr>
  </table>

  <div class="fax__notes">
    <div class="fax__flags">
      <div class="fax__flag" style="width:87px"><span class="fax__box"></span>Urgent</div>
      <div class="fax__flag" style="width:85px"><span class="fax__box"></span>For Review</div>
      <div class="fax__flag" style="width:96px"><span class="fax__box"></span>Please Comment</div>
      <div class="fax__flag" style="width:82px"><span class="fax__box"></span>Please Reply</div>
      <div class="fax__flag" style="flex:1"><span class="fax__box"></span>Please Recycle</div>
    </div>
    <p class="fax__comments-label">COMMENTS:</p>
  </div>

  <footer class="contact">
    <div class="contact__group">
      <div class="contact__line"><span class="contact__icon"></span>(07) 5120 4417</div>
      <div class="contact__line"><span class="contact__icon"></span>(07) 5120 4418</div>
    </div>
    <div class="contact__group">
      <div class="contact__line"><span class="contact__icon"></span>info@corvella.com</div>
      <div class="contact__line"><span class="contact__icon"></span>www.corvella.com</div>
    </div>
    <div class="contact__group">
      <div>Suite 4, 208B</div>
      <div>Riverton QLD</div>
    </div>
  </footer>
</section>

</body>
</html>
```